political advertisement for magazine

9.135 in 12.125 in. My wife is running for Judge. She needs an ad for an African-American Magazine ASAP . The ad is about a testimonial by one of her clients that makes her relatable to the African-American community. I am uploading the text for the testimonial, the picture of my wife and her client, her logo, a possible backdrop and also a slogan.

This is going in a church publication geared toward the African American Community

• The image of all the people in the back. On top of that image, you have "The people stand behind Lorena for Circuit Court Judge". Also you have a letter from her client with a picture of both of them. Also include the vote for Lorena logo and her headshot. The above is just my idea if you have an idea that is totally different but portrays that Lorena is for the people, I am ok with that too. thanks!

```html
<!DOCTYPE html>
<html lang="en">
<head>
<meta charset="utf-8">
<title>Lorena for Circuit Court Judge – Magazine Ad</title>
<link href="https://fonts.googleapis.com/css2?family=Arimo:wght@400;700&family=Crimson+Pro:wght@500&family=Roboto:wght@300;400&display=swap" rel="stylesheet">
<style>
  :root{
    --navy:#1f3a75;
    --red:#e4232b;
    --white:#ffffff;
    --page:#ffffff;
    --ink:#1f3a75;
    --grey:#8a8f98;
  }
  html,body{margin:0;padding:0;width:1200px;height:849px;overflow:hidden;background:var(--page);}
  body{-webkit-font-smoothing:antialiased;-moz-osx-font-smoothing:grayscale;}
  .ad{
    position:absolute;left:291px;top:14px;width:617px;height:820px;
    background:var(--white);box-shadow:0 1px 6px rgba(0,0,0,.28);overflow:hidden;
    font-family:"Arimo",Arial,sans-serif;
  }
  .crowd-photo{
    position:absolute;left:0;top:0;width:617px;height:378px;
    background:linear-gradient(135deg,#b88a6e 0%,#6f8f4e 30%,#c9a28a 55%,#4f6a3a 75%,#d7b7a0 100%);
  }
  .band{position:absolute;left:0;top:378px;width:617px;height:155px;background:var(--navy);}
  .headshot{
    position:absolute;left:50px;top:312px;width:266px;height:266px;border-radius:50%;
    background:radial-gradient(circle at 50% 38%,#d9b59c 0%,#9a6e52 30%,#3a2e2c 62%,#1e1c1e 100%);
    box-shadow:0 3px 8px rgba(0,0,0,.35);
  }
  .headline{position:absolute;left:326px;top:413px;width:260px;text-align:center;color:var(--white);white-space:nowrap;}
  .headline .kicker{font-family:"Roboto",sans-serif;font-weight:300;font-size:11.5px;letter-spacing:2.2px;margin:0;}
  .headline .name{font-family:"Crimson Pro",serif;font-weight:500;font-size:50px;line-height:42px;color:var(--red);margin:2px 0 0;letter-spacing:1px;}
  .headline .office{font-family:"Roboto",sans-serif;font-weight:300;font-size:14px;letter-spacing:2.4px;margin:4px 0 0;}
  .logo-name{
    position:absolute;left:48px;top:640px;width:190px;text-align:center;
    font-family:"Crimson Pro",serif;font-weight:500;font-size:24px;line-height:28px;color:var(--red);
  }
  .client-photo{
    position:absolute;left:262px;top:587px;width:138px;height:138px;border:3px solid var(--navy);
    background:linear-gradient(160deg,#3f6b35 0%,#7a9a55 45%,#d9cfc6 75%,#b8c6d4 100%);
  }
  .testimonial{position:absolute;left:411px;top:586px;width:158px;color:var(--ink);font-size:7.3px;line-height:9px;}
  .testimonial p{margin:0 0 3px;color:var(--ink);}
  .testimonial .signature{font-weight:700;}
  .disclaimer{position:absolute;left:0;top:774px;width:617px;text-align:center;color:var(--grey);font-size:5.8px;line-height:8px;margin:0;}
</style>
</head>
<body>
<main class="ad">
  <div class="crowd-photo" role="img" aria-label="Grid of smiling portraits of diverse community members"></div>
  <div class="band"></div>
  <div class="headshot" role="img" aria-label="Headshot of Lorena smiling in a dark blazer and pearl necklace"></div>

  <header class="headline">
    <p class="kicker">THE PEOPLE STAND BEHIND</p>
    <h1 class="name">LORENA</h1>
    <p class="office">FOR CIRCUIT COURT JUDGE</p>
  </header>

  <div class="logo-name">Lorena Whitfield Ames</div>

  <div class="client-photo" role="img" aria-label="Lorena shaking hands with her client outdoors in front of flowering bushes"></div>

  <section class="testimonial">
    <p>For the past few years, Lorena Whitfield Ames has been my lawyer. She has always strived to provide excellence in legal services. Her almost encyclopedic knowledge of the law makes for a flawless, precise, navigation of the legal system, with results.</p>
    <p>She is the epitome of professionalism, that is aptly balanced by her calm persona. Her empathy is more than commendable, and her legal experience unmatched.</p>
    <p>Lorena Whitfield Ames is truly one of kind, deserving of all accolades, appointments, and accomplishments.</p>
    <p>Yours Truly,</p>
    <p class="signature">Daniel Brooks</p>
  </section>

  <p class="disclaimer">POLITICAL ADVERTISEMENT PAID FOR AND APPROVED BY THE COMMITTEE TO ELECT LORENA WHITFIELD AMES,<br>NO PARTY AFFILIATION, FOR CIRCUIT COURT JUDGE</p>
</main>
</body>
</html>
```